Website Hero Image Redesign Brief
The current hero image appears too busy and lacks the elegance that reflects our brand. We would like to create a new, refined hero image for our real estate company's website.
Requirements:
Clean, elegant, and modern look
Should represent premium real estate sales
Use either our existing images from the website or create a custom design
Focus on sophistication, trust, and exclusivity
Ensure the image works well with overlay text and call-to-action buttons

Goal:
The new hero image should immediately convey professionalism, elegance, and the premium nature of our real estate services, while maintaining a calm and inviting visual impression.

Website: https://www.lindqvoltwohnen.example/

```html
<!DOCTYPE html>
<html lang="en">
<head>
<meta charset="utf-8">
<title>Lindqvolt Wohnen – Your Local Real Estate Professional</title>
<link rel="stylesheet" href="https://fonts.googleapis.com/css2?family=Montserrat:wght@700&family=Poppins:wght@400;500;600&display=swap">
<style>
  :root {
    --nav-top: #c9dfe9;
    --nav-bottom: #e3ecf1;
    --nav-text: #1c2a33;
    --nav-active: #0d1418;
    --sky-top: #8fc9e8;
    --sky-low: #c3deea;
    --house-warm: #7a6250;
    --lawn: #4f7a34;
    --lawn-dark: #2e4a1f;
    --shade: rgba(22, 32, 38, 0.72);
    --white: #ffffff;
    --brand-green: #3fae4e;
    --button-top: #5cb86a;
    --button-bottom: #2f8f45;
  }
  * { margin: 0; padding: 0; box-sizing: border-box; }
  html, body { width: 1200px; height: 535px; overflow: hidden; }
  body { font-family: "Poppins", sans-serif; background: var(--white); }

  .hero { position: relative; width: 1200px; height: 535px; overflow: hidden; }

  .site-nav {
    position: absolute; top: 0; left: 0; width: 1200px; height: 87px;
    background: linear-gradient(180deg, var(--nav-top), var(--nav-bottom));
    z-index: 3;
  }
  .site-nav a {
    position: absolute; top: 37px;
    font-size: 13.4px; font-weight: 400; color: var(--nav-text);
    text-decoration: none; letter-spacing: 0.1px; white-space: nowrap;
  }
  .site-nav a.is-active { font-weight: 600; color: var(--nav-active); }

  .hero-photo {
    position: absolute; top: 87px; left: 0; width: 1200px; height: 448px;
    background:
      radial-gradient(ellipse 360px 90px at 660px 290px, rgba(240, 170, 80, 0.55), transparent 70%),
      linear-gradient(180deg,
        var(--sky-top) 0%, var(--sky-low) 36%,
        var(--house-warm) 48%, #8a6b52 62%,
        var(--lawn) 72%, #6f8f5a 86%, var(--lawn-dark) 100%);
  }

  .hero-shade { position: absolute; top: 87px; left: 0; width: 1200px; height: 448px; z-index: 1; }

  .hero-content { position: absolute; left: 67px; top: 0; z-index: 2; color: var(--white); }

  .brand-name {
    position: absolute; top: 128px; left: 0; white-space: nowrap;
    display: flex; align-items: center; gap: 8px;
    font-family: "Poppins", sans-serif; font-weight: 600; font-size: 30px;
    color: var(--brand-green); line-height: 1;
  }
  .brand-mark { width: 12px; height: 12px; background: var(--brand-green); }

  .hero-title {
    position: absolute; top: 206px; left: -2px; white-space: nowrap;
    font-family: "Montserrat", sans-serif; font-weight: 700;
    font-size: 53px; line-height: 62px; letter-spacing: -1.6px;
  }

  .hero-tagline {
    position: absolute; top: 403px; left: 0; white-space: nowrap;
    font-size: 14px; font-weight: 500;
  }

  .cta-button {
    position: absolute; top: 445px; left: 0; width: 155px; height: 43px;
    display: flex; align-items: center; justify-content: center;
    border-radius: 8px;
    background: linear-gradient(180deg, var(--button-top), var(--button-bottom));
    color: var(--white); font-size: 14.5px; font-weight: 600; text-decoration: none;
  }
</style>
</head>
<body>
<main class="hero">
  <nav class="site-nav">
    <a class="is-active" href="#" style="left:187px">HOME PAGE</a>
    <a href="#" style="left:313px">ABOUT US</a>
    <a href="#" style="left:428px">SALE</a>
    <a href="#" style="left:507px">OUR REFERENCE</a>
    <a href="#" style="left:659px">OBJECTS</a>
    <a href="#" style="left:767px">CALL-BACK SERVICE</a>
    <a href="#" style="left:948px">CONTACT</a>
  </nav>

  <div class="hero-photo" role="img" aria-label="Photograph of a large lit country house at dusk with a curving path across a green lawn"></div>

  <svg class="hero-shade" viewBox="0 0 1200 448" aria-hidden="true">
    <polygon points="0,0 405,0 630,448 0,448" fill="var(--shade)"/>
  </svg>

  <div class="hero-content">
    <div class="brand-name"><span class="brand-mark"></span>Lindqvolt Wohnen</div>
    <h1 class="hero-title">YOUR LOCAL<br>REAL ESTATE<br>PROFESSIONAL</h1>
    <p class="hero-tagline">Rooted in Meilen - on the move on Lake Zurich</p>
    <a class="cta-button" href="#">CONTACT US</a>
  </div>
</main>
</body>
</html>
```